Website incl. html for real estate project

We need the design and implementation of a website for a real estate project. Condominiums are built, which are sold.
We upload the sales brochure. The website should be based on the design of the sales brochure.
There are three houses with 5 apartments each. It should be rendered like this. The structure of the menu should be roughly as follows. Most information about the content is either in the appendix as a picture or in the brochure (PDF)):
Home (page 4-5 from the brochure)
House A
house B
house c
overview
basement
Municipal elections (page 6-7 in the brochure pdf)
Contact
Please use Roboto Regular as font.
And one page should give an overview of all apartments with the prices, the living space, etc. as on the file overview2.jpg.
If you go to the House A, House B, or House C menus, a page should come up with the details for that house only. The pages in the brochure are:
House A (Page 10-11)
House B (page 22-23)
House C (page 34-35)
The individual apartments should each be shown on a property page. There the plan / floor plan of the apartment and the pictures from the inside should be shown. As with the object page.jpg attachment.
Für die Designer... Mehr Zeit...
Coded - Design and coding required
1 page

```html
<!DOCTYPE html>
<html lang="de">
<head>
<meta charset="utf-8">
<title>Wohnpark am Ahorn</title>
<link href="https://fonts.googleapis.com/css2?family=Roboto:wght@400;500;700&display=swap" rel="stylesheet">
<style>
:root{
  --navy:#0d3a52;
  --blue:#006a94;
  --red:#e30613;
  --text:#222;
  --grey:#efefef;
}
*{box-sizing:border-box;margin:0;padding:0}
html,body{width:1200px;height:3513px;overflow:hidden}
body{font-family:'Roboto',sans-serif;color:var(--text);background:#fff;position:relative}
.btn{position:absolute;background:var(--red);color:#fff;font-size:12px;font-weight:700;display:flex;align-items:center;justify-content:center}

/* header */
.header{position:absolute;left:0;top:0;width:1200px;height:72px;background:#fff}
.brand{position:absolute;left:71px;top:20px;display:flex;align-items:center;gap:10px;color:var(--blue);font-size:19px;font-weight:500}
.brand-mark{width:14px;height:14px;background:var(--red)}
.topbar{position:absolute;left:657px;top:0;width:543px;height:27px;background:var(--navy);color:#fff;font-size:12px;display:flex;align-items:center;gap:90px;padding-left:40px}
.topbar span{display:flex;align-items:center;gap:8px}
.nav{position:absolute;right:71px;top:45px;display:flex;gap:39px;font-size:12px}
.nav .active{color:var(--red)}

/* hero */
.hero{position:absolute;left:0;top:72px;width:1200px;height:565px;background:var(--navy)}
.hero-img{position:absolute;left:71px;top:53px;width:1058px;height:512px;background:linear-gradient(180deg,#cfd9e2 0%,#dfe4e6 40%,#b9bcb8 60%,#6f9a4a 75%,#4f7d32 100%)}
.pin{position:absolute;width:50px;height:50px;border-radius:50%;background:#fff;color:var(--red);font-size:10px;font-weight:700;display:flex;align-items:center;justify-content:center;box-shadow:0 2px 6px rgba(0,0,0,.3)}
.arrow{position:absolute;width:44px;height:44px;border-radius:50%;background:#fff;display:flex;align-items:center;justify-content:center;box-shadow:0 2px 6px rgba(0,0,0,.3)}

/* intro */
.intro{position:absolute;left:0;top:637px;width:1200px;height:409px;background:var(--blue);color:#fff;text-align:center}
.intro h1{font-weight:400;font-size:30px;margin-top:62px}
.intro p{font-size:22px;line-height:36px;margin-top:10px}

/* overview table */
.labels{position:absolute;left:71px;top:875px;width:129px;height:467px}
.labels .cap{position:absolute;left:0;top:0;width:129px;height:171px;background:#fff}
.label{position:absolute;left:12px;width:102px;font-size:12px;font-weight:700;border-bottom:1px solid #555;padding-left:9px}
.card{position:absolute;top:875px;width:304px;height:467px;background:#fff;border:1px solid #ccc}
.card-img{height:82px;background:linear-gradient(180deg,#d8e0e6,#c9ccc9 60%,#a9aca8)}
.card-head{height:68px;background:var(--navy);color:#fff;font-size:24px;font-weight:700;display:flex;align-items:center;justify-content:center}
.row{position:absolute;left:5px;right:5px;font-size:12px;display:grid;grid-template-columns:78px 48px 1fr 80px;line-height:15px}
.row .price{text-align:right}
.sep{position:absolute;left:10px;right:10px;height:1px;background:#555}

/* living */
.living-photo{position:absolute;left:102px;top:1443px;width:457px;height:435px;background:linear-gradient(180deg,#e9e9e8,#cfccc7 60%,#bdb8b1)}
.living-overlay{position:absolute;left:71px;top:1443px}
.living-text{position:absolute;left:668px;top:1518px;width:445px}
.living-text h2{font-weight:400;font-size:30px;line-height:43px}
.living-text p{font-size:13.5px;line-height:25.5px;margin-top:20px}

/* quote */
.quote{position:absolute;left:0;top:1940px;width:1200px;height:340px;background:radial-gradient(ellipse at 60% 50%,#e9101c,#d50512 70%,#c80410);color:#fff;text-align:center}
.quote .mark{font-size:130px;font-weight:700;line-height:1;margin-top:78px;height:76px;font-family:Georgia,serif}
.quote p{font-size:22px;line-height:38px;margin-top:36px}

/* gallery */
.gallery-title{position:absolute;left:0;top:2350px;width:1200px;text-align:center;font-size:30px;font-weight:400}
.shot{position:absolute;top:2423px;width:298px;height:169px;border:3px solid #fff;box-shadow:0 2px 8px rgba(0,0,0,.3);background:linear-gradient(180deg,#f1f1f0,#dcd9d4 60%,#c8c1b6)}
.garrow{position:absolute;top:2489px;width:33px;height:33px;border-radius:50%;display:flex;align-items:center;justify-content:center}

/* contact */
.contact{position:absolute;left:0;top:2705px;width:1200px;height:395px;background:var(--grey)}
.map-ring{position:absolute;left:140px;top:2649px;width:420px;height:420px;border-radius:50%;background:var(--red)}
.map{position:absolute;left:155px;top:2649px;width:427px;height:427px;border-radius:50%;background:radial-gradient(circle at 50% 45%,#dbe9cf,#c6ddb2 60%,#b3d1a0)}
.contact-text{position:absolute;left:690px;top:2762px;width:395px}
.contact-text h2{font-weight:400;font-size:30px}
.contact-text p{font-size:12px;line-height:20px;margin-top:16px}
.field{position:absolute;background:#fff;font-size:12px;padding:10px 12px}

/* footer */
.footer{position:absolute;left:0;top:3100px;width:1200px;height:413px;background:var(--navy);color:#fff}
.footer .brand{color:#fff;left:71px;top:80px}
.footer h4{position:absolute;font-weight:400;font-size:16px}
.foot-desc{position:absolute;left:71px;top:150px;width:245px;font-size:14px;line-height:22.5px}
.fitem{position:absolute;display:flex;gap:14px;font-size:14px;line-height:18px;align-items:flex-start}
.ficon{width:22px;height:22px;border-radius:50%;flex:none;display:flex;align-items:center;justify-content:center}
.sicon{width:20px;height:20px;border-radius:50%;background:#fff;flex:none}
.foot-nav{position:absolute;left:0;top:300px;width:1200px;display:flex;justify-content:center;gap:22px;font-size:14px}
.copy{position:absolute;left:0;top:362px;width:1200px;text-align:center;font-size:12px}
.copy span{color:var(--red)}
</style>
</head>
<body>

<header class="header">
  <div class="brand"><span class="brand-mark"></span>Brunnhalde Immobilien AG</div>
  <div class="topbar">
    <span><svg width="13" height="10" viewBox="0 0 13 10"><rect x="0.5" y="0.5" width="12" height="9" fill="none" stroke="#fff"/><path d="M0.5 0.5 L6.5 5.5 L12.5 0.5" fill="none" stroke="#fff"/></svg>info@brunnhalde-immo.ch</span>
    <span><svg width="11" height="11" viewBox="0 0 24 24"><path fill="#fff" d="M6.6 10.8a15 15 0 0 0 6.6 6.6l2.2-2.2c.3-.3.7-.4 1-.2 1.1.4 2.3.6 3.6.6.6 0 1 .4 1 1V20c0 .6-.4 1-1 1A17 17 0 0 1 3 4c0-.6.4-1 1-1h3.5c.6 0 1 .4 1 1 0 1.3.2 2.5.6 3.6.1.3 0 .7-.2 1z"/></svg>+41 61 000 12 34</span>
  </div>
  <nav class="nav">
    <span class="active">Startseite</span><span>Haus A</span><span>Haus B</span><span>Haus C</span><span>Untergeschoss</span><span>Gemeinde Riedhalden</span><span>Kontakt</span>
  </nav>
</header>

<section class="hero">
  <div class="hero-img" role="img" aria-label="Visualisierung der drei Mehrfamilienhäuser im Grünen"></div>
  <div class="pin" style="left:285px;top:206px">Haus C</div>
  <div class="pin" style="left:665px;top:251px">Haus B</div>
  <div class="pin" style="left:857px;top:236px">Haus A</div>
  <div class="arrow" style="left:50px;top:300px"><svg width="14" height="14" viewBox="0 0 14 14"><path d="M9 2 L4 7 L9 12" fill="none" stroke="#222" stroke-width="2.5"/></svg></div>
  <div class="arrow" style="left:1108px;top:300px"><svg width="14" height="14" viewBox="0 0 14 14"><path d="M5 2 L10 7 L5 12" fill="none" stroke="#e30613" stroke-width="2.5"/></svg></div>
</section>

<section class="intro">
  <h1>Wohnpark am Ahorn</h1>
  <p>Hochwertige and moderne Eigentumswohnungen an der<br>Talstrasse/Mattenweg in Riedhalden</p>
</section>

<section class="overview">
  <div class="labels">
    <div class="cap"></div>
    <div class="label" style="top:166px;height:36px">Attika</div>
    <div class="label" style="top:228px;height:42px">Obergeshoss</div>
    <div class="label" style="top:290px;height:41px">Obergeshoss</div>
    <div class="label" style="top:353px;height:51px">Erdgeschoss</div>
    <div class="label" style="top:416px;height:52px">Erdgeschoss</div>
  </div>

  <div class="card" style="left:205px">
    <div class="card-img" role="img" aria-label="Ansicht Haus A"></div>
    <div class="card-head">Haus A</div>
    <div class="row" style="top:171px"><span>4.5 Zimmer</span><span>108m²</span><span>105m²<br>Sonnenerrasse</span><span class="price">945'000CHF</span></div>
    <div class="sep" style="top:204px"></div>
    <div class="row" style="top:232px"><span>3.5 Zimmer</span><span>108m²</span><span>105m²<br>Balkon</span><span class="price">754'800CHF</span></div>
    <div class="sep" style="top:266px"></div>
    <div class="row" style="top:293px"><span>4.5 Zimmer</span><span>108m²</span><span>105m²<br>Balkon</span><span class="price">640'000CHF</span></div>
    <div class="sep" style="top:327px"></div>
    <div class="row" style="top:353px"><span>4.5 Zimmer</span><span>108m²</span><span>105m²<br>Gedeckter<br>sitzplatz</span><span class="price">657'000CHF</span></div>
    <div class="sep" style="top:402px"></div>
    <div class="row" style="top:421px"><span>4.5 Zimmer</span><span>108m²</span><span>105m²<br>Sonnenerrasse</span><span class="price">765'000CHF</span></div>
  </div>

  <div class="card" style="left:515px">
    <div class="card-img" role="img" aria-label="Ansicht Haus B"></div>
    <div class="card-head">Haus B</div>
    <div class="row" style="top:171px"><span>4.5 Zimmer</span><span>108m²</span><span>105m²<br>Sonnenerrasse</span><span class="price">945'000CHF</span></div>
    <div class="sep" style="top:204px"></div>
    <div class="row" style="top:232px"><span>3.5 Zimmer</span><span>108m²</span><span>105m²<br>Balkon</span><span class="price">754'800CHF</span></div>
    <div class="sep" style="top:266px"></div>
    <div class="row" style="top:293px"><span>4.5 Zimmer</span><span>108m²</span><span>105m²<br>Balkon</span><span class="price">640'000CHF</span></div>
    <div class="sep" style="top:327px"></div>
    <div class="row" style="top:353px"><span>4.5 Zimmer</span><span>108m²</span><span>105m²<br>Gedeckter<br>sitzplatz</span><span class="price">657'000CHF</span></div>
    <div class="sep" style="top:402px"></div>
    <div class="row" style="top:421px"><span>4.5 Zimmer</span><span>108m²</span><span>105m²<br>Sonnenerrasse</span><span class="price">765'000CHF</span></div>
  </div>

  <div class="card" style="left:826px">
    <div class="card-img" role="img" aria-label="Ansicht Haus C"></div>
    <div class="card-head">Haus C</div>
    <div class="row" style="top:171px"><span>4.5 Zimmer</span><span>108m²</span><span>105m²<br>Sonnenerrasse</span><span class="price">945'000CHF</span></div>
    <div class="sep" style="top:204px"></div>
    <div class="row" style="top:232px"><span>3.5 Zimmer</span><span>108m²</span><span>105m²<br>Balkon</span><span class="price">754'800CHF</span></div>
    <div class="sep" style="top:266px"></div>
    <div class="row" style="top:293px"><span>4.5 Zimmer</span><span>108m²</span><span>105m²<br>Balkon</span><span class="price">640'000CHF</span></div>
    <div class="sep" style="top:327px"></div>
    <div class="row" style="top:353px"><span>4.5 Zimmer</span><span>108m²</span><span>105m²<br>Gedeckter<br>sitzplatz</span><span class="price">657'000CHF</span></div>
    <div class="sep" style="top:402px"></div>
    <div class="row" style="top:421px"><span>4.5 Zimmer</span><span>108m²</span><span>105m²<br>Sonnenerrasse</span><span class="price">765'000CHF</span></div>
  </div>

  <div class="btn" style="left:300px;top:1334px;width:115px;height:39px">Learn More</div>
  <div class="btn" style="left:610px;top:1334px;width:115px;height:39px">Learn More</div>
  <div class="btn" style="left:921px;top:1334px;width:115px;height:39px">Learn More</div>
</section>

<section class="living">
  <div class="living-photo" role="img" aria-label="Helles Wohnzimmer mit Sofa und Essbereich"></div>
  <svg class="living-overlay" width="533" height="435" viewBox="0 0 533 435">
    <polygon points="0,224 140,74 533,218 533,435 0,435" fill="#e30613" opacity="0.62"/>
  </svg>
  <div class="living-text">
    <h2>Wohnen in<br>Riedhalden bei Birsau</h2>
    <p>In Riedhalden fi nden Sie die sprichwörtlich ländliche Ruhe, eine hohe Wohnqualität, sowie eine sehr gute Erschliessung durch des Öffen-tlichen- wie auch den Individualverkehr in Kombination mit einem intakten Dorfl eben.</p>
  </div>
  <div class="btn" style="left:670px;top:1747px;width:115px;height:38px">Learn More</div>
</section>

<section class="quote">
  <div class="mark">“</div>
  <p>Egal ob für Paare, Singles, Rentneroder Familien. In der Gemeinde<br>Riedhalden im Wohnpark am Ahornfi nden Sie Ihr neues Zuhause zum Wohlfühlen.</p>
</section>

<section class="gallery">
  <h2 class="gallery-title">Die Wohnungen</h2>
  <div class="garrow" style="left:72px;background:#444"><svg width="12" height="12" viewBox="0 0 12 12"><path d="M8 2 L4 6 L8 10" fill="none" stroke="#fff" stroke-width="2.2"/></svg></div>
  <div class="shot" style="left:132px" role="img" aria-label="Essbereich mit Wohnzimmer"></div>
  <div class="shot" style="left:451px" role="img" aria-label="Offener Wohnraum mit Esstisch"></div>
  <div class="shot" style="left:770px" role="img" aria-label="Küche mit Wohnbereich"></div>
  <div class="garrow" style="left:1095px;background:var(--red)"><svg width="12" height="12" viewBox="0 0 12 12"><path d="M4 2 L8 6 L4 10" fill="none" stroke="#fff" stroke-width="2.2"/></svg></div>
</section>

<section class="contact"></section>
<div class="map-ring"></div>
<div class="map" role="img" aria-label="Karte der Region mit Standort"></div>
<div class="contact-text">
  <h2>Contact Us</h2>
  <p>It is a long established fact that a reader will be distracted by the readable content of a page when looking at its layout.</p>
</div>
<div class="field" style="left:690px;top:2869px;width:180px;height:34px">Name</div>
<div class="field" style="left:880px;top:2869px;width:181px;height:34px">Email</div>
<div class="field" style="left:690px;top:2910px;width:371px;height:87px">Message</div>
<div class="btn" style="left:690px;top:3015px;width:117px;height:38px">Submit Now</div>

<footer class="footer">
  <div class="brand"><span class="brand-mark" style="background:#fff"></span>Brunnhalde Immobilien AG</div>
  <p class="foot-desc">Die Überbauung mit drei Mehrfamilienhäusern und insgesamt 15 Eigentumswohnungen entsteht zwischen der Talstrasse .</p>

  <h4 style="left:390px;top:62px">Quick Link</h4>
  <div class="fitem" style="left:390px;top:106px"><span class="ficon" style="background:var(--red)"><svg width="10" height="12" viewBox="0 0 10 12"><path d="M5 0a4 4 0 0 0-4 4c0 3 4 8 4 8s4-5 4-8a4 4 0 0 0-4-4z" fill="#fff"/><circle cx="5" cy="4" r="1.5" fill="#e30613"/></svg></span><span>Brunnhalde Immobilien AG<br>Schweiz</span></div>
  <div class="fitem" style="left:390px;top:164px"><span class="ficon" style="background:#1d4d66"><svg width="10" height="10" viewBox="0 0 24 24"><path fill="#fff" d="M6.6 10.8a15 15 0 0 0 6.6 6.6l2.2-2.2c.3-.3.7-.4 1-.2 1.1.4 2.3.6 3.6.6.6 0 1 .4 1 1V20c0 .6-.4 1-1 1A17 17 0 0 1 3 4c0-.6.4-1 1-1h3.5c.6 0 1 .4 1 1 0 1.3.2 2.5.6 3.6.1.3 0 .7-.2 1z"/></svg></span><span>+41 61 000 12 34</span></div>
  <div class="fitem" style="left:390px;top:206px"><span class="ficon" style="background:#1d4d66"><svg width="10" height="8" viewBox="0 0 13 10"><rect x="0.5" y="0.5" width="12" height="9" fill="none" stroke="#fff"/><path d="M0.5 0.5 L6.5 5.5 L12.5 0.5" fill="none" stroke="#fff"/></svg></span><span>info@brunnhalde-immo.ch</span></div>

  <h4 style="left:691px;top:62px">Get Social</h4>
  <div class="fitem" style="left:693px;top:110px"><span class="sicon"></span><span>Instagram</span></div>
  <div class="fitem" style="left:693px;top:146px"><span class="sicon"></span><span>Facebook</span></div>

  <h4 style="left:874px;top:62px">Newsletter</h4>
  <div class="field" style="left:874px;top:105px;width:255px;height:39px;color:#333">Enter Your Mail ID</div>
  <div class="btn" style="left:874px;top:154px;width:116px;height:38px">Subscribe Now</div>

  <nav class="foot-nav">
    <span>Startseite</span><span>Kontakt</span><span>Haus A</span><span>Haus B</span><span>Haus C</span><span>Untergeschoss</span><span>Gemeinde</span><span>Riedhalden</span><span>Impressum</span><span>Datenschutz</span>
  </nav>
  <p class="copy">© 2022 <span>brunnhalde</span>. All rights reserved</p>
</footer>

</body>
</html>
```